Best in class business looking for best in class stationery that accurately reflects the brand image we are trying to build as the brand expands throughout the country. The Varying items should be an eye catching design that makes even the simplest letter or small business card stand out in the crowd.

Target Market(s)

Professionals

Industry/Entity Type

Real Estate

Other font styles liked:
• See atttached logo

Requirements
Must have
• Letterhead
• Business cards
• Envelopes
• Labels for larger mailings
Nice to have
• Folders
• Notebook
Should not have
• Stale design elements

```html
<!DOCTYPE html>
<html lang="en">
<head>
<meta charset="utf-8">
<title>Ridgeline Property Group — Letterhead</title>
<link href="https://fonts.googleapis.com/css2?family=Arimo:wght@400;700&family=Open+Sans:wght@400&display=swap" rel="stylesheet">
<style>
  :root {
    --backdrop: #bdbbdf;
    --paper: #ffffff;
    --brand: #2a3a9c;
    --ink: #1c1c22;
    --muted: #8a8a92;
  }
  * { box-sizing: border-box; margin: 0; padding: 0; }
  html, body { width: 1200px; height: 784px; overflow: hidden; }
  body {
    background: var(--backdrop);
    display: flex;
    align-items: center;
    justify-content: center;
    font-family: "Arimo", Arial, sans-serif;
  }
  .letterhead {
    position: relative;
    width: 540px;
    height: 740px;
    background: var(--paper);
    box-shadow: 0 6px 18px rgba(60, 55, 120, .25);
    padding: 46px 40px 0 40px;
  }
  .brand {
    display: flex;
    justify-content: flex-end;
    align-items: center;
    gap: 8px;
    margin-bottom: 26px;
  }
  .brand-mark {
    width: 14px; height: 14px;
    background: var(--brand);
  }
  .brand-name {
    font-size: 15px;
    font-weight: 700;
    color: var(--brand);
    letter-spacing: .04em;
    text-transform: uppercase;
  }
  .letter-body {
    text-align: right;
    font-size: 10.5px;
    line-height: 1.5;
    color: var(--ink);
  }
  .letter-body p { margin-bottom: 16px; }
  .footer {
    position: absolute;
    left: 40px; right: 40px; bottom: 34px;
    display: flex;
    justify-content: space-between;
    align-items: center;
    font-family: "Open Sans", Arial, sans-serif;
    font-size: 7px;
    color: var(--muted);
    white-space: nowrap;
  }
  .contact-item { display: flex; align-items: center; gap: 4px; }
  .contact-icon { width: 10px; height: 10px; flex: none; }
</style>
</head>
<body>
  <main class="letterhead">
    <header class="brand">
      <span class="brand-mark"></span>
      <span class="brand-name">Ridgeline Property Group</span>
    </header>

    <section class="letter-body">
      <p>Lorem Ipsum is simply dummy text of the printing and typesetting industry. Lorem Ipsum has been the industry's standard dummy text ever since the 1500s, when an unknown printer took a galley of type and scrambled it to make a type specimen book. It has survived not only five centuries, but also the leap into electronic typesetting, remaining essentially unchanged. It was popularised in the 1960s with the release of Fontline sheets containing Lorem Ipsum passages, and more recently with desktop publishing software like PageCraft including versions of Lorem Ipsum.</p>
      <p>It is a long established fact that a reader will be distracted by the readable content of a page when looking at its layout. The point of using Lorem Ipsum is that it has a more-or-less normal distribution of letters, as opposed to using 'Content here, content here', making it look like readable English. Many desktop publishing packages and web page editors now use Lorem Ipsum as their default model text, and a search for 'lorem ipsum' will uncover many web sites still in their infancy. Various versions have evolved over the years, sometimes by accident, sometimes on purpose (injected humour and the like).</p>
      <p>Contrary to popular belief, Lorem Ipsum is not simply random text. It has roots in a piece of classical Latin literature from 45 BC, making it over 2000 years old. Daniel Harrow, a Latin professor at Westbrook College in Oregon, looked up one of the more obscure Latin words, consectetur, from a Lorem Ipsum passage, and going through the cites of the word in classical literature, discovered the undoubtable source. Lorem Ipsum comes from sections 1.10.32 and 1.10.33 of an old Latin treatise on ethics, using its structures to generate Lorem Ipsum which looks reasonable. The generated Lorem Ipsum is therefore always free from repetition, injected humour, or non-characteristic words etc.</p>
    </section>

    <footer class="footer">
      <span class="contact-item">
        <svg class="contact-icon" viewBox="0 0 12 12"><circle cx="6" cy="6" r="6" fill="#2a3a9c"/><path d="M6 2.5a2 2 0 0 0-2 2c0 1.6 2 4.5 2 4.5s2-2.9 2-4.5a2 2 0 0 0-2-2z" fill="#fff"/></svg>
        000 Elm Ave, Suite 300, Aurora, US 0000
      </span>
      <span class="contact-item">
        <svg class="contact-icon" viewBox="0 0 12 12"><circle cx="6" cy="6" r="6" fill="#2a3a9c"/><path d="M4 3h1.3l.6 1.6-.8.6a4 4 0 0 0 1.7 1.7l.6-.8L9 6.7V8a1 1 0 0 1-1 1A5 5 0 0 1 3 4a1 1 0 0 1 1-1z" fill="#fff"/></svg>
        555.010.2400
      </span>
      <span class="contact-item">
        <svg class="contact-icon" viewBox="0 0 12 12"><circle cx="6" cy="6" r="6" fill="#2a3a9c"/><rect x="3" y="5" width="6" height="3.5" fill="#fff"/><rect x="4" y="3" width="4" height="2" fill="#fff"/></svg>
        555.010.2401
      </span>
      <span class="contact-item">
        <svg class="contact-icon" viewBox="0 0 12 12"><circle cx="6" cy="6" r="6" fill="#2a3a9c"/><rect x="3" y="4" width="6" height="4.2" fill="#fff"/><path d="M3 4l3 2.3L9 4" fill="none" stroke="#2a3a9c" stroke-width=".7"/></svg>
        hello@ridgelinepg.com
      </span>
      <span class="contact-item">
        <svg class="contact-icon" viewBox="0 0 12 12"><circle cx="6" cy="6" r="6" fill="#2a3a9c"/><circle cx="6" cy="6" r="3" fill="none" stroke="#fff" stroke-width=".8"/><path d="M3 6h6M6 3c-1.5 1.8-1.5 4.2 0 6M6 3c1.5 1.8 1.5 4.2 0 6" fill="none" stroke="#fff" stroke-width=".6"/></svg>
        ridgelinepg.com
      </span>
    </footer>
  </main>
</body>
</html>
```